Informational Site for Advanced Chemistry R&D

The company develops oxidation chemistry for air, water, fuel pollution controls. The site has been prototyped at www.velmirlab.net. Take a look. Now, the task is to design it for eye-catching beauty with use of color, on-page scroll-driven color transition and parallax effects. Should capture the themes: high technology, wow it's beautiful, modern, uncluttered, clean urban environment.

Target Market(s)

China Environmentally Conscious Government and Industry,

Industry/Entity Type

It Company

Number of Pages Required

3 page

Font styles to use
Sans Serif

Requirements
Must have
• Parallax effects, desktop compatible, Rich, Modern, Simple, Graphic
Nice to have
• Mobile Phone Compatible
Should not have
• Flash, or anything that is slow to load or requires high bandwidth

```html
<!DOCTYPE html>
<html lang="en">
<head>
<meta charset="utf-8">
<title>Velmir Lab — New Ideas for a Cleaner World</title>
<link rel="stylesheet" href="https://fonts.googleapis.com/css2?family=Open+Sans:wght@400;600;700;800&display=swap">
<style>
:root{
  --teal:#2db4ae;
  --teal-dark:#23928d;
  --blue:#1f6ca8;
  --ink:#333;
  --muted:#666;
  --light:#f3f3f3;
  --white:#fff;
  --line:#d6d6d6;
  --badge:#dcdcdc;
}
*{margin:0;padding:0;box-sizing:border-box}
html,body{width:1200px;height:2894px;overflow:hidden}
body{font-family:"Open Sans",Arial,sans-serif;color:var(--ink);background:var(--white);position:relative}

/* hero */
.hero{position:absolute;left:0;top:0;width:1200px;height:660px;
  background:linear-gradient(135deg,#6e7a72 0%,#98a583 30%,#7e9b4a 55%,#a5b58a 75%,#7c7466 100%)}
.brand{position:absolute;left:96px;top:40px;display:flex;flex-direction:column;align-items:center;gap:6px}
.brand-dot{width:96px;height:64px;border-radius:50%;border:4px solid var(--white)}
.brand-name{font-size:34px;font-weight:600;color:var(--white);letter-spacing:-0.5px}
.nav{position:absolute;top:108px;left:598px;display:flex}
.nav a{color:var(--white);text-decoration:none;font-size:15px;font-weight:600;position:relative}
.nav a.home::after{content:"";position:absolute;left:0;right:0;bottom:-9px;height:2px;background:var(--teal)}
.search{position:absolute;left:1058px;top:110px}
.hero-title{position:absolute;left:0;width:1200px;top:296px;text-align:center;color:var(--white);
  font-size:40px;font-weight:800;line-height:56px;text-shadow:0 2px 6px rgba(0,0,0,.35)}
.dots{position:absolute;top:574px;left:566px;display:flex;gap:10px}
.dots span{width:15px;height:15px;border-radius:50%;background:var(--white)}
.dots span.on{background:var(--teal)}

/* about */
.about{position:absolute;top:660px;left:0;width:1200px;height:400px;background:var(--light)}
.section-title{font-size:25px;font-weight:700;color:var(--blue);text-align:center}
.about .section-title{margin-top:56px}
.about p{width:760px;margin:18px auto 0;text-align:center;font-size:11.5px;line-height:23px;color:var(--muted)}
.pillars{position:absolute;top:200px;left:300px;width:600px;display:flex;justify-content:space-between}
.pillar{width:140px;text-align:center}
.pillar svg{height:96px}
.pillar span{display:block;margin-top:12px;font-size:17px;color:var(--ink)}

/* oxidation */
.oxidation{position:absolute;top:1000px;left:0;width:1200px;height:518px;
  background:linear-gradient(100deg,#5d6a59 0%,#7e8a6a 35%,#6a6d5a 60%,#b7a78e 85%,#c4b8a8 100%)}
.wave{position:absolute;top:0;left:0}
.diagram{position:absolute;left:180px;top:120px;width:300px;height:360px;border-radius:40%;
  background:radial-gradient(circle,rgba(250,205,30,.55) 0%,rgba(250,205,30,.2) 50%,rgba(250,205,30,0) 72%)}
.ox-text{position:absolute;left:528px;top:122px;width:460px;color:var(--white)}
.ox-text h2{font-size:25px;font-weight:700}
.ox-lead{margin-top:16px;color:var(--teal);font-size:14px;font-weight:600;line-height:20px}
.ox-list{list-style:none;margin-top:42px}
.ox-list li{font-size:13px;display:flex;align-items:center;gap:14px;height:34px}
.ox-list li::before{content:"";width:12px;height:12px;border-radius:50%;border:2px solid var(--white);
  background:radial-gradient(circle,var(--white) 30%,transparent 35%)}
.ox-body{margin-top:26px;font-size:13px;line-height:24px;text-align:justify}
.btn{display:inline-block;background:var(--teal);color:var(--white);font-size:13px;text-align:center;text-decoration:none}
.ox-text .btn{margin-top:30px;width:128px;height:46px;line-height:46px}

/* solutions */
.solutions{position:absolute;top:1518px;left:0;width:1200px;height:482px;background:var(--white)}
.solutions .section-title{margin-top:46px}
.cards{position:absolute;top:108px;left:96px;width:1008px;display:flex;justify-content:space-between}
.card{width:242px;text-align:center}
.card h3{font-size:17px;font-weight:600;color:var(--teal);white-space:nowrap}
.card p{margin-top:6px;font-size:12.5px;line-height:20px;color:var(--ink);height:70px}
.card-frame{margin-top:16px;padding:9px;background:var(--white);box-shadow:0 0 6px rgba(0,0,0,.15);position:relative}
.card-photo{height:178px}
.photo-plant{background:linear-gradient(160deg,#3f4a55,#7b858d 50%,#2e3238)}
.photo-worker{background:linear-gradient(160deg,#93a0a9,#3e5870 50%,#8a8f88)}
.photo-stacks{background:linear-gradient(180deg,#5f6d7c,#9ba5ae 50%,#1e2228)}
.photo-outfall{background:linear-gradient(180deg,#39452d,#a58e5c 55%,#4c7fae)}
.card-frame .btn{position:absolute;left:61px;top:74px;width:120px;height:42px;line-height:42px}

/* partners */
.partners{position:absolute;top:2000px;left:0;width:1200px;height:228px;background:var(--light);display:flex}
.partner{text-align:center;position:relative;border-left:2px solid var(--line)}
.partner:first-child{flex:0 0 349px;border-left:none}
.partner:nth-child(2),.partner:nth-child(3){flex:0 0 251px}
.partner:last-child{flex:1}
.partner .badge{margin:28px auto 0;height:120px;display:flex;align-items:center;justify-content:center}
.badge-shape{width:110px;height:110px;background:var(--badge)}
.badge-shape.round{border-radius:50%}
.korva{gap:8px}
.korva i{width:14px;height:14px;background:var(--blue);border-radius:50%}
.korva b{font-size:20px;font-weight:700;color:var(--blue);white-space:nowrap}
.partner span{display:block;margin-top:20px;font-size:17px;line-height:22px;color:var(--ink)}

/* contact */
.contact{position:absolute;top:2228px;left:0;width:1200px;height:579px}
.map{position:absolute;inset:0;background:linear-gradient(120deg,#d9d6c8 0%,#e6e1cf 45%,#c9d4d6 70%,#9db9d4 100%)}
.contact-panel{position:absolute;left:131px;top:0;width:468px;height:579px;background:rgba(255,255,255,.94);padding:26px 26px 0 26px}
.contact-panel h2{font-size:25px;font-weight:700;color:var(--blue)}
.contact-intro{margin-top:14px;font-size:12px;line-height:20px;color:var(--muted)}
.contact-cols{display:flex;margin-top:22px}
.contact-cols > div{width:210px}
.contact-cols h4,.form-label{font-size:16px;font-weight:600;color:var(--blue)}
.contact-cols p{margin-top:12px;font-size:12.5px;line-height:22px;color:var(--ink)}
.phone{margin-top:18px;font-size:12.5px}
.form-label{margin-top:30px}
.field{position:absolute;background:var(--teal);color:rgba(255,255,255,.85);font-size:14px;padding:10px}
.send{position:absolute;left:164px;top:519px;width:407px;height:46px;line-height:46px;text-align:center;
  background:linear-gradient(180deg,#49c6c0,#239f99);color:#0f5f5b;font-weight:700;font-size:16px;letter-spacing:1px}

/* footer */
.footer{position:absolute;top:2807px;left:0;width:1200px;height:87px;background:var(--teal);color:var(--white)}
.footer .copy{position:absolute;left:131px;top:34px;font-size:12.5px;font-weight:600}
.social{position:absolute;left:944px;top:32px;display:flex;align-items:center;gap:10px;font-size:11px;font-weight:600}
.social i{width:16px;height:16px;border-radius:50%;background:var(--white)}
</style>
</head>
<body>

<header class="hero" role="img" aria-label="Photograph of green liquid in laboratory test tubes held by a gloved hand, with chemical structure line drawings overlaid">
  <div class="brand"><div class="brand-dot"></div><div class="brand-name">VelmirLab</div></div>
  <nav class="nav">
    <a class="home" href="#">Home</a>
    <a href="#" style="margin-left:54px">Technology</a>
    <a href="#" style="margin-left:50px">Products</a>
    <a href="#" style="margin-left:50px">Contact</a>
  </nav>
  <svg class="search" width="18" height="18" viewBox="0 0 18 18" aria-label="Search"><circle cx="7" cy="7" r="5.5" fill="none" stroke="#fff" stroke-width="2.4"/><line x1="11" y1="11" x2="16.5" y2="16.5" stroke="#fff" stroke-width="2.6" stroke-linecap="round"/></svg>
  <h1 class="hero-title">NEW IDEAS FOR<br>A CLEANER WORLD</h1>
  <div class="dots"><span></span><span class="on"></span><span></span></div>
</header>

<section class="about">
  <h2 class="section-title">ABOUT VELMIR LAB</h2>
  <p>Korva Systems is engaged in the sales, service and support of environmental solutions for industry and government. With offices in Lanmere, Dovecrest, Harrowfield, and Tennport, Korva Systems is among the most advanced and rapidly growing companies offering solutions for air, water and fuel environmental compliance. Velmir Lab Corporation supports these solutions with research and development.</p>
  <div class="pillars">
    <div class="pillar">
      <svg viewBox="0 0 70 96" width="70"><path d="M35 4 C30 26 6 46 6 64 a29 29 0 0 0 58 0 C64 46 40 26 35 4Z" fill="#2db4ae"/><path d="M18 66 a17 17 0 0 0 14 16" fill="none" stroke="#fff" stroke-width="4" stroke-linecap="round"/></svg>
      <span>Water</span>
    </div>
    <div class="pillar">
      <svg viewBox="0 0 100 96" width="100"><circle cx="44" cy="52" r="34" fill="none" stroke="#2db4ae" stroke-width="5"/><circle cx="44" cy="52" r="7" fill="#2db4ae"/><path d="M44 52 L44 24 M44 52 L70 60 M44 52 L22 72" stroke="#2db4ae" stroke-width="6" stroke-linecap="round"/><path d="M70 22 H94 V42 H76" fill="none" stroke="#2db4ae" stroke-width="5"/></svg>
      <span>Air</span>
    </div>
    <div class="pillar">
      <svg viewBox="0 0 80 96" width="80"><rect x="8" y="6" width="46" height="84" rx="4" fill="#2db4ae"/><rect x="15" y="14" width="32" height="22" fill="#fff"/><rect x="2" y="86" width="58" height="8" fill="#2db4ae"/><path d="M54 40 H64 V74 a5 5 0 0 0 10 0 V28 L64 18" fill="none" stroke="#2db4ae" stroke-width="5"/></svg>
      <span>Fuel</span>
    </div>
  </div>
</section>

<section class="oxidation" role="img" aria-label="Photograph of a gloved hand working with laboratory glassware, softly blurred">
  <svg class="wave" width="1200" height="130" viewBox="0 0 1200 130" aria-hidden="true"><path d="M0 0 H1200 V150 C1120 60 1000 15 850 12 C640 8 460 80 0 88 Z" fill="#f3f3f3"/></svg>
  <div class="diagram" role="img" aria-label="Illustration of oxidation reaction species circled in yellow around a hydroxyl radical"></div>
  <div class="ox-text">
    <h2>ADVANCED OXIDATION</h2>
    <p class="ox-lead">Advanced Oxidation refers to a variety of techniques employing the Hydroxyl Radical, an energetic, highly reactive cousin of the water molecule:</p>
    <ul class="ox-list">
      <li>To add oxygen to inorganic molecules</li>
      <li>To remove hydrogen from organic molecules</li>
    </ul>
    <p class="ox-body">These transformations convert important industrial contaminants into reactive forms that can be captured or that disintegrate into harmless end products.</p>
    <a class="btn" href="#">View More</a>
  </div>
</section>

<section class="solutions">
  <h2 class="section-title">SOLUTIONS</h2>
  <div class="cards">
    <article class="card">
      <h3>Fuel Oil Desulfurization</h3>
      <p>Our proprietary low temperature and pressure advanced oxidation catalytic process reliably removes...</p>
      <div class="card-frame"><div class="card-photo photo-plant" role="img" aria-label="Photograph of an industrial refinery plant"></div><a class="btn" href="#">View More</a></div>
    </article>
    <article class="card">
      <h3>Volatile Organic Compunds</h3>
      <p>Alkanes, alkenes, halogenated hydrocarbons, esters, aldehydes, polycyclic ...</p>
      <div class="card-frame"><div class="card-photo photo-worker" role="img" aria-label="Photograph of a worker handling chemical containers"></div></div>
    </article>
    <article class="card">
      <h3>Flue Gas Scrubbing</h3>
      <p>Desulfurization and denitrification using our proprietary flue gas advanced oxidation catalytic process (FGAOC).</p>
      <div class="card-frame"><div class="card-photo photo-stacks" role="img" aria-label="Photograph of smoking factory chimneys"></div></div>
    </article>
    <article class="card">
      <h3>Wastewater Treatment</h3>
      <p>Desulfurization and denitrification using our proprietary flue gas advanced oxidation catalytic process (FGAOC).</p>
      <div class="card-frame"><div class="card-photo photo-outfall" role="img" aria-label="Photograph of wastewater flowing from an outfall pipe"></div></div>
    </article>
  </div>
</section>

<section class="partners">
  <div class="partner"><div class="badge korva"><i></i><b>Korva Systems</b></div><span>Our sales partner in<br>China</span></div>
  <div class="partner"><div class="badge"><div class="badge-shape" role="img" aria-label="Partner badge"></div></div><span>Our construction<br>partner in China</span></div>
  <div class="partner"><div class="badge"><div class="badge-shape round" role="img" aria-label="Partner badge"></div></div><span>Our technology<br>partner in China</span></div>
  <div class="partner"><div class="badge"><div class="badge-shape round" role="img" aria-label="Partner badge"></div></div><span>Our technology<br>partner in China</span></div>
</section>

<section class="contact">
  <div class="map" role="img" aria-label="Road map of the area around the company office"></div>
  <div class="contact-panel">
    <h2>Contact US</h2>
    <p class="contact-intro">We welcome inquiries regarding the licensing, distribution, and purchase of our products, systems, and technologies.</p>
    <div class="contact-cols">
      <div><h4>Address</h4><p>Velmir Lab Corporation Alder<br>Brook, Marston County, U.S.A.</p><p class="phone">Phone : +1 555 014 2290</p></div>
      <div><h4>Email</h4><p>info@velmirlab.net<br>support@velmirlab.net</p></div>
    </div>
    <p class="form-label">FORM</p>
  </div>
  <div class="field" style="left:164px;top:330px;width:193px;height:46px">Name</div>
  <div class="field" style="left:376px;top:330px;width:195px;height:46px">Email</div>
  <div class="field" style="left:164px;top:397px;width:407px;height:101px">Message</div>
  <div class="send">SEND</div>
</section>

<footer class="footer">
  <p class="copy">© 2016 Velmir Lab All Rights Reserved.</p>
  <div class="social">Social Media : <i></i><i></i><i></i></div>
</footer>

</body>
</html>
```